dog treat packaging

packaging for dog treat brand named Tollivan
below images of whsat the packages will look like / please post designs on same packaging

Industry/Entity Type

Pet

Requirements
Must have
• funky / cool /fun / unique / playful

```html
<!DOCTYPE html>
<html lang="en">
<head>
<meta charset="utf-8">
<title>Tollivan Beef &amp; Cheese Bite Size Treats</title>
<link rel="stylesheet" href="https://fonts.googleapis.com/css2?family=Oswald:wght@400;500;600&family=Open+Sans:wght@400;700&family=Lobster&display=swap">
<style>
  :root {
    --backdrop: #e9e9e9;
    --kraft: #d6cfb7;
    --kraft-edge: #c4bca2;
    --zip: #bdb59b;
    --ink: #3a1e12;
    --brand-blue: #2ea3dc;
    --orange: #f08a12;
    --green: #3fa346;
    --green-dark: #1f6e2a;
    --cloud-green: #2e9a45;
    --white: #ffffff;
    --black: #141414;
    --divider: #e0563a;
  }
  * { box-sizing: border-box; margin: 0; padding: 0; }
  html, body {
    width: 1200px; height: 1200px; overflow: hidden;
    background: var(--backdrop);
  }
  .canvas { position: relative; width: 1200px; height: 1200px; }

  .pouch {
    position: absolute; left: 302px; top: 94px;
    width: 620px; height: 1018px;
  }
  .pouch__shapes, .pouch__badge { position: absolute; left: 0; top: 0; }

  .pouch__illustration {
    position: absolute; left: 190px; top: 470px;
    width: 325px; height: 410px;
    border-radius: 48% 52% 42% 46%;
    background: radial-gradient(ellipse at 50% 35%, #e0b040 0%, #c98a2a 50%, #3b8ed0 80%, #2a6fb0 100%);
  }

  .tear-note {
    position: absolute; left: 0; right: 0; top: 66px;
    text-align: center;
    font: 500 18px/24px "Oswald", sans-serif;
    color: var(--ink);
  }

  .brand {
    position: absolute; left: 52px; top: 222px;
    display: flex; align-items: center; gap: 12px;
    transform: rotate(-6deg); transform-origin: left center;
  }
  .brand__dot { width: 18px; height: 18px; border-radius: 50%; background: var(--brand-blue); }
  .brand__name {
    font: 600 62px/1 "Oswald", sans-serif;
    color: var(--brand-blue);
  }

  .claims {
    position: absolute; left: 326px; top: 250px; width: 264px;
    display: flex; align-items: stretch;
    font: 400 9px/1.4 "Open Sans", sans-serif;
    color: var(--ink); text-align: center;
  }
  .claim { flex: 1; display: flex; flex-direction: column; align-items: center; gap: 3px; }
  .claim strong { font-weight: 700; }
  .claims__divider { width: 1px; background: var(--divider); margin: 0 4px; }

  .flavour {
    position: absolute; left: 84px; top: 326px;
    transform: rotate(-13deg); transform-origin: left top;
    font: 400 72px/0.88 "Lobster", cursive;
    color: var(--white);
    text-shadow: 3px 3px 0 var(--ink);
  }
  .flavour span { display: block; white-space: nowrap; }
  .flavour__lead { font-size: 60px; }
  .flavour__line2 { padding-left: 14px; }
  .flavour__line3 { padding-left: 40px; }

  .thought {
    position: absolute; left: 372px; top: 386px;
    width: 170px; transform: rotate(-8deg);
    font: 500 19px/1.25 "Oswald", sans-serif;
    color: var(--white); text-align: center;
  }

  .bite-size {
    position: absolute; left: 176px; top: 926px;
    width: 160px; height: 36px; line-height: 36px;
    text-align: center; transform: rotate(-10deg);
    font: 600 25px "Oswald", sans-serif; color: var(--ink);
  }
  .net-weight {
    position: absolute; left: 350px; top: 956px;
    width: 104px; height: 40px; border-radius: 20px 20px 0 0;
    background: var(--black); color: var(--white);
    font: 400 18px/40px "Oswald", sans-serif; text-align: center;
  }
</style>
</head>
<body>
<main class="canvas">
  <section class="pouch" aria-label="Tollivan treat pouch front">
    <svg class="pouch__shapes" width="620" height="1018" viewBox="0 0 620 1018" aria-hidden="true">
      <rect class="pouch__edge" x="0" y="0" width="620" height="1018" fill="var(--kraft-edge)"/>
      <rect class="pouch__panel" x="24" y="42" width="572" height="970" fill="var(--kraft)"/>
      <g class="zip-lines" stroke="var(--zip)" stroke-width="3" fill="none">
        <line x1="28" y1="112" x2="592" y2="112"/>
        <line x1="28" y1="124" x2="592" y2="124"/>
        <line x1="28" y1="142" x2="592" y2="142"/>
      </g>
      <path class="blob-orange" fill="var(--orange)"
        d="M110 330 C170 300 300 300 390 320 C480 340 520 400 512 500 C505 590 470 660 410 700 C340 740 200 730 130 690 C70 650 54 560 60 480 C66 410 70 350 110 330 Z"/>
      <path class="blob-green" fill="var(--green)"
        d="M230 500 C320 470 440 480 510 530 C575 580 580 670 555 740 C590 810 575 900 505 945 C420 990 290 985 200 950 C130 920 100 860 120 800 C95 730 130 650 170 600 C190 555 205 515 230 500 Z"/>
      <g class="cloud" fill="var(--cloud-green)" stroke="var(--green-dark)" stroke-width="5">
        <path d="M380 385 C365 360 395 340 420 350 C438 330 480 332 496 352 C526 348 545 372 534 394 C556 414 540 448 512 444 C500 466 462 468 444 454 C420 470 385 462 380 440 C356 436 355 400 380 385 Z"/>
        <circle cx="536" cy="472" r="6"/>
        <circle cx="548" cy="498" r="8"/>
        <circle cx="550" cy="532" r="12"/>
        <circle cx="534" cy="572" r="17"/>
      </g>
    </svg>

    <div class="pouch__illustration" role="img"
      aria-label="Illustration of a happy cartoon puppy leaning over a blue bowl filled with beef and cheese roll treats"></div>

    <svg class="pouch__badge" width="620" height="1018" viewBox="0 0 620 1018" aria-hidden="true">
      <g class="bone" transform="translate(256 944) rotate(-10)">
        <g fill="var(--black)">
          <rect x="-62" y="-23" width="124" height="46"/>
          <circle cx="-64" cy="-17" r="25"/><circle cx="-64" cy="17" r="25"/>
          <circle cx="64" cy="-17" r="25"/><circle cx="64" cy="17" r="25"/>
        </g>
        <g fill="var(--white)">
          <rect x="-62" y="-18" width="124" height="36"/>
          <circle cx="-64" cy="-17" r="20"/><circle cx="-64" cy="17" r="20"/>
          <circle cx="64" cy="-17" r="20"/><circle cx="64" cy="17" r="20"/>
        </g>
      </g>
    </svg>

    <p class="tear-note">Tear me to open and re-seal me for freshness!</p>

    <div class="brand">
      <span class="brand__dot"></span>
      <span class="brand__name">Tollivan</span>
    </div>

    <div class="claims">
      <div class="claim">
        <svg width="22" height="20" viewBox="0 0 26 24" aria-hidden="true" fill="none" stroke="var(--ink)" stroke-width="1.6">
          <path d="M3 14 L6 9 L18 9 L21 4 L24 6 L22 11 L20 12 L20 21 M7 9 L7 21 M11 14 L11 21 M17 14 L17 21"/>
        </svg>
        <span>Keep your pet dog<br><strong>healthy, active &amp; happy!</strong></span>
      </div>
      <div class="claims__divider"></div>
      <div class="claim">
        <svg width="20" height="20" viewBox="0 0 24 24" aria-hidden="true" fill="none" stroke="var(--ink)" stroke-width="1.6">
          <ellipse cx="12" cy="16" rx="5" ry="4"/>
          <circle cx="6" cy="9" r="2"/><circle cx="10" cy="5" r="2"/>
          <circle cx="14" cy="5" r="2"/><circle cx="18" cy="9" r="2"/>
        </svg>
        <span>Provide balanced nutrition<br>and strengthen your pet's<br><strong>immune system</strong></span>
      </div>
    </div>

    <h1 class="flavour">
      <span class="flavour__lead">mmm...</span>
      <span class="flavour__line2">Beef &amp;</span>
      <span class="flavour__line3">Cheese</span>
    </h1>

    <p class="thought">Loved by puppies<br>and small dogs</p>

    <p class="bite-size">Bite Size</p>
    <p class="net-weight">300 GM</p>
  </section>
</main>
</body>
</html>
```